Bref créative
Business Card design for Property Management Company
Harborlight Stewards
Professional
Corwin Talbot
P.O. Box K-4183
Nassau, Bahamas
corwin@harborlightstewardsgroup.com

```html
<!DOCTYPE html>
<html lang="en">
<head>
<meta charset="utf-8">
<title>Harborlight Stewards Stationery</title>
<link rel="stylesheet" href="https://fonts.googleapis.com/css2?family=Cinzel:wght@500&family=Open+Sans:wght@400;600&display=swap">
<style>
:root{
  --stage:#eeeff1;
  --paper:#ffffff;
  --blue-deep:#0b3a6c;
  --blue:#1d5f9e;
  --blue-light:#4e8cc8;
  --gold:#f2b43a;
  --ink:#1f2a36;
  --muted:#6b7785;
  --faint:#e7edf4;
}
*{box-sizing:border-box;margin:0;padding:0}
html,body{width:1200px;height:936px;overflow:hidden}
body{background:var(--stage);position:relative;font-family:"Open Sans",sans-serif;color:var(--ink)}
.piece{position:absolute;background:var(--paper);overflow:hidden}
.piece svg.wave{position:absolute;left:0;width:100%}
.brand{position:absolute;display:flex;align-items:center;gap:8px}
.brand-dot{border-radius:50%;background:var(--blue);flex:none}
.brand-name{font-family:"Cinzel",serif;font-weight:500;color:var(--blue-deep);line-height:1;white-space:nowrap}

.letterhead{left:182px;top:63px;width:386px;height:543px}
.letterhead .wave{top:0;height:120px}
.letterhead .brand{left:24px;top:40px}
.letterhead .brand-dot{width:26px;height:26px}
.letterhead .brand-name{font-size:13px}
.letterhead .faint-mark{position:absolute;left:50%;top:220px;transform:translateX(-50%);display:flex;flex-direction:column;align-items:center;gap:10px}
.letterhead .faint-mark .brand-dot{width:110px;height:110px;background:var(--faint)}
.letterhead .contact{position:absolute;left:24px;bottom:26px;font-size:6.5px;line-height:1.55;color:var(--muted)}

.folder{left:632px;top:50px;width:416px;height:569px}
.folder .wave{bottom:0;height:150px}
.folder .brand{left:50%;top:238px;transform:translateX(-50%);gap:14px}
.folder .brand-dot{width:60px;height:60px}
.folder .brand-name{font-size:27px}

.card-front{left:43px;top:652px;width:179px;height:106px;border-radius:5px}
.card-front .wave{top:0;height:40px}
.card-front .brand{left:12px;top:10px;gap:5px}
.card-front .brand-dot{width:14px;height:14px}
.card-front .brand-name{font-size:7.5px;color:var(--paper)}
.card-front .person{position:absolute;left:12px;top:48px;font-size:5.4px;line-height:1.5;color:var(--muted)}
.card-front .person strong{color:var(--ink);font-weight:600;font-size:6px}

.card-back{left:43px;top:776px;width:179px;height:108px;border-radius:5px;background:var(--blue)}
.card-back .wave{top:0;height:108px}
.card-back .brand-dot{position:absolute;left:50%;top:36px;width:26px;height:26px;transform:translateX(-50%);background:var(--gold)}
.card-back .url{position:absolute;left:0;right:0;bottom:14px;text-align:center;font-size:5px;color:var(--paper);letter-spacing:.05em}

.envelope-front{left:263px;top:662px;width:429px;height:210px}
.envelope-front .brand{left:24px;top:22px}
.envelope-front .brand-dot{width:24px;height:24px}
.envelope-front .brand-name{font-size:12px}
.envelope-front .tagline{position:absolute;left:56px;top:52px;font-size:6px;color:var(--muted);letter-spacing:.04em}

.envelope-back{left:738px;top:662px;width:432px;height:210px}
.envelope-back .wave{top:0;height:100px}
.envelope-back .url{position:absolute;left:0;right:0;top:36px;text-align:center;font-family:"Cinzel",serif;font-size:10px;color:var(--paper);letter-spacing:.04em}
</style>
</head>
<body>

<section class="piece letterhead">
  <svg class="wave" viewBox="0 0 386 120" preserveAspectRatio="none" aria-hidden="true">
    <defs><linearGradient id="lhBlue" x1="0" x2="1"><stop offset="0" stop-color="#4e8cc8"/><stop offset="1" stop-color="#0b3a6c"/></linearGradient></defs>
    <path d="M120 0H386V70C330 40 280 78 220 72C180 68 150 40 120 0Z" fill="url(#lhBlue)"/>
    <path d="M0 58C90 90 180 92 260 72C310 60 350 62 386 74" fill="none" stroke="#1d5f9e" stroke-width="2"/>
  </svg>
  <div class="brand"><span class="brand-dot"></span><span class="brand-name">Harborlight Stewards</span></div>
  <div class="faint-mark"><span class="brand-dot"></span></div>
  <div class="contact">
    <div>P.O. Box K-4183</div>
    <div>Nassau, Bahamas</div>
    <div>Tel 242 555 0184</div>
    <div>Fax 242 555 0185</div>
    <div>corwin@harborlightstewardsgroup.com</div>
  </div>
</section>

<section class="piece folder">
  <div class="brand"><span class="brand-dot"></span><span class="brand-name">Harborlight Stewards</span></div>
  <svg class="wave" viewBox="0 0 416 150" preserveAspectRatio="none" aria-hidden="true">
    <defs><linearGradient id="fdBlue" x1="0" x2="1"><stop offset="0" stop-color="#0b3a6c"/><stop offset="1" stop-color="#1d5f9e"/></linearGradient></defs>
    <path d="M0 30C60 70 150 90 250 60C320 38 370 20 416 10V150H0Z" fill="url(#fdBlue)"/>
    <path d="M0 46C80 86 170 98 260 72C330 52 380 38 416 34" fill="none" stroke="#ffffff" stroke-width="3"/>
  </svg>
</section>

<section class="piece card-front">
  <svg class="wave" viewBox="0 0 179 40" preserveAspectRatio="none" aria-hidden="true">
    <path d="M0 0H179V24C130 14 90 40 40 34C20 32 8 28 0 26Z" fill="#1d5f9e"/>
    <path d="M0 30C40 40 90 34 130 24C150 20 168 22 179 26" fill="none" stroke="#4e8cc8" stroke-width="1.2"/>
  </svg>
  <div class="brand"><span class="brand-dot" style="background:var(--paper)"></span><span class="brand-name">Harborlight Stewards</span></div>
  <div class="person">
    <div><strong>Corwin Talbot</strong></div>
    <div>P.O. Box K-4183, Nassau, Bahamas</div>
    <div>Tel 242 555 0184</div>
    <div>Fax 242 555 0185</div>
    <div>corwin@harborlightstewardsgroup.com</div>
  </div>
</section>

<section class="piece card-back">
  <svg class="wave" viewBox="0 0 179 108" preserveAspectRatio="none" aria-hidden="true">
    <path d="M0 70C50 90 110 60 179 80V108H0Z" fill="#0b3a6c"/>
  </svg>
  <span class="brand-dot"></span>
  <div class="url">www.harborlightstewardsgroup.com</div>
</section>

<section class="piece envelope-front">
  <div class="brand"><span class="brand-dot"></span><span class="brand-name">Harborlight Stewards</span></div>
  <div class="tagline">Property Management &amp; Stewardship</div>
</section>

<section class="piece envelope-back">
  <svg class="wave" viewBox="0 0 432 100" preserveAspectRatio="none" aria-hidden="true">
    <path d="M0 0H432V84C360 60 280 98 200 92C120 86 60 70 0 80Z" fill="#1d5f9e"/>
    <path d="M0 88C70 78 130 96 210 98C290 100 360 70 432 90" fill="none" stroke="#0b3a6c" stroke-width="2"/>
  </svg>
  <div class="url">WWW.HARBORLIGHTSTEWARDSGROUP.COM</div>
</section>

</body>
</html>
```